Business Card Design for Cybersecurity Company - Quorvent Systems

We need a business card design for our new cybersecurity company, Quorvent. We’re going for a clean, hi tech look that feels modern, premium, and trustworthy. We want a design that really stands out and makes people say WOW when we hand it over!

Quorvent delivers reliable IT support and managed services for small and mid sized businesses. We help companies stay secure, efficient, and connected through proactive monitoring, cybersecurity services, cloud management, and remote support.

Target Market(s)

Designers should target small and mid sized businesses that need dependable cybersecurity and IT support.

Industry/Entity Type

Cybersecurity, Managed Service Provider, IT services

Contact Information for Business Card

Contact information

Requirements
Must have
• The card should look clean, modern, and tech focused, with the Quorvent logo, clear contact info, and strong readability. It needs to feel premium and professional while still keeping a simple layout that fits a cybersecurity and IT brand.
Nice to have
• Nice to have elements include subtle touches that give the card a modern, tech feel, along with a layout that works well in different background styles.
Should not have
• The card should avoid clutter, loud graphics, or anything that takes attention away from the logo and contact details.

```html
<!DOCTYPE html>
<html lang="en">
<head>
<meta charset="utf-8">
<title>Quorvent Systems — Business Card</title>
<link href="https://fonts.googleapis.com/css2?family=Lato:wght@400;700&display=swap" rel="stylesheet">
<style>
  :root {
    --backdrop: #1b1b1d;
    --card-deep: #0a0d2e;
    --card-light: #151b4d;
    --brand-blue: #2f80f2;
    --brand-violet: #8a3be6;
    --text-light: #e9ecf7;
    --text-soft: #b9bed6;
  }
  * { margin: 0; padding: 0; box-sizing: border-box; }
  html, body {
    width: 1200px; height: 939px; overflow: hidden;
    background: var(--backdrop);
    font-family: "Lato", sans-serif;
  }
  .canvas { position: relative; width: 1200px; height: 939px; }

  .card {
    position: absolute;
    width: 540px; height: 309px;
    border-radius: 18px;
    background: linear-gradient(135deg, var(--card-deep) 0%, var(--card-light) 100%);
    box-shadow: 0 18px 40px rgba(0,0,0,.55);
    overflow: hidden;
  }
  .card--front { left: 90px; top: 110px; }
  .card--back  { left: 570px; top: 500px; }

  /* Front */
  .brand {
    position: absolute; inset: 0;
    display: flex; align-items: center; justify-content: center; gap: 16px;
  }
  .brand__dot {
    width: 46px; height: 46px; border-radius: 50%;
    background: var(--brand-blue);
  }
  .brand__name {
    display: block;
    font-weight: 700; font-size: 46px; letter-spacing: 1px;
    color: var(--text-light);
    line-height: 1;
  }
  .brand__sub {
    display: block;
    font-weight: 400; font-size: 15px; letter-spacing: 8px;
    color: var(--text-light);
    margin-top: 8px;
  }

  /* Back */
  .corner-mark {
    position: absolute; top: 26px; right: 28px;
    font-weight: 700; font-size: 14px; letter-spacing: .5px;
    color: var(--brand-blue);
  }
  .identity {
    position: absolute; right: 276px; top: 118px;
    text-align: right;
  }
  .identity__name {
    font-weight: 700; font-size: 24px; color: var(--brand-blue);
    letter-spacing: .3px; white-space: nowrap; line-height: 1.15;
  }
  .identity__role {
    font-size: 15px; color: var(--brand-violet); margin-top: 2px;
    white-space: nowrap;
  }
  .divider {
    position: absolute; left: 280px; top: 104px;
    width: 2px; height: 72px;
    background: linear-gradient(var(--brand-blue), var(--brand-violet));
  }
  .contacts {
    position: absolute; left: 300px; top: 100px;
    list-style: none;
  }
  .contacts li {
    display: flex; align-items: center; gap: 10px;
    font-size: 14.5px; color: var(--text-soft);
    height: 26px; white-space: nowrap;
  }
  .contacts svg { width: 14px; height: 14px; fill: var(--brand-blue); flex: none; }
  .website {
    position: absolute; left: 0; right: 0; bottom: 40px;
    text-align: center; font-size: 14px; color: var(--text-soft);
    letter-spacing: .5px;
  }
  .website strong { color: var(--text-light); font-weight: 700; }
</style>
</head>
<body>
<main class="canvas">

  <section class="card card--front" aria-label="Card front">
    <div class="brand">
      <span class="brand__dot"></span>
      <div>
        <span class="brand__name">Quorvent</span>
        <span class="brand__sub">Systems</span>
      </div>
    </div>
  </section>

  <section class="card card--back" aria-label="Card back">
    <span class="corner-mark">Quorvent</span>

    <div class="identity">
      <p class="identity__name">DANA WHITFIELD</p>
      <p class="identity__role">Owner / CEO</p>
    </div>

    <span class="divider"></span>

    <ul class="contacts">
      <li>
        <svg viewBox="0 0 24 24" aria-hidden="true"><path d="M6.6 10.8a15.1 15.1 0 0 0 6.6 6.6l2.2-2.2c.3-.3.7-.4 1-.2 1.1.4 2.3.6 3.6.6.6 0 1 .4 1 1V20c0 .6-.4 1-1 1A17 17 0 0 1 3 4c0-.6.4-1 1-1h3.5c.6 0 1 .4 1 1 0 1.3.2 2.5.6 3.6.1.3 0 .7-.2 1z"/></svg>
        (855) 408-QVNT
      </li>
      <li>
        <svg viewBox="0 0 24 24" aria-hidden="true"><path d="M7 1h10a2 2 0 0 1 2 2v18a2 2 0 0 1-2 2H7a2 2 0 0 1-2-2V3a2 2 0 0 1 2-2zm0 3v14h10V4zm5 15.5a1 1 0 1 0 0 2 1 1 0 0 0 0-2z"/></svg>
        (813) 555-0182
      </li>
      <li>
        <svg viewBox="0 0 24 24" aria-hidden="true"><path d="M2 5h20v14H2zm2 2v.5l8 5 8-5V7zm0 2.8V17h16V9.8l-8 5z"/></svg>
        dana@quorvent.com
      </li>
    </ul>

    <p class="website">www.<strong>Quorvent</strong>.com</p>
  </section>

</main>
</body>
</html>
```